High-End Bifold Brochure for Aesthetics Medspa Business

I need a print-ready, bifold brochure designed for a high-end, luxurious Aesthetics/Medspa practice.

The brochure will showcase the latest IV Therapy content (6 options included in MENU.docx), and exclusive Vitamin B12+ wellness shot content (included in LS PDF). It should also include the business logo and basic office contact options.

The design should be clean, modern, and appealing with a light design. It should flow nicely and compliment the website theme/design. Preferably, having the 6 IV treatments inside bifold, with B12 shot on back/outside page. For easy viewing.

I have attached a few licensed images, if you think they will incorporate into the design nicely. Otherwise, please ignore them. If needed, I can send more.

https://lunavelleskincareclinic.com/
Brand purple: #491c64
Fonts used on site:
Josefin Sans
Montserrat

Size should be 6.5 x 9 using specs on Quillapress's template page (Half Fold design)
https://www.quillapress.com/resources/templates

• Montserrat, Josefin Sans, or similar

• Content included in MENU + B12 shot content on PDF.
Similar feel to the website, High-end, modern, luxurious

```html
<!DOCTYPE html>
<html lang="en">
<head>
<meta charset="utf-8">
<title>The Drip Atelier – IV Therapy &amp; B12 Brochure</title>
<link href="https://fonts.googleapis.com/css2?family=Josefin+Sans:wght@300;400;600;700&family=Montserrat:wght@400;500;600;700&display=swap" rel="stylesheet">
<style>
  :root{
    --brand-purple:#491c64;
    --purple-mid:#6a3a8a;
    --purple-soft:#b79bc9;
    --ink:#2b2430;
    --muted:#5a5160;
    --paper:#ffffff;
    --page-bg:#eeecef;
  }
  *{box-sizing:border-box;margin:0;padding:0}
  html,body{width:839px;height:1200px;overflow:hidden;background:var(--page-bg)}
  body{position:relative;font-family:"Montserrat",Arial,sans-serif;color:var(--ink)}

  .spread{position:absolute;left:22px;width:795px;background:var(--paper);box-shadow:0 2px 10px rgba(0,0,0,.12);overflow:hidden}
  .spread--outside{top:70px;height:500px}
  .spread--inside{top:610px;height:530px}

  /* outside spread */
  .hero-photo{position:absolute;left:0;top:0;width:400px;height:100%;
    background:radial-gradient(ellipse at 55% 55%,#e9dcd2 0%,#f5efea 45%,#fbf9f8 75%);}
  .b12-panel{position:absolute;left:410px;top:0;width:385px;height:100%;padding:28px 28px 0 22px}
  .b12-title{font-family:"Josefin Sans",Arial,sans-serif;font-weight:600;color:var(--brand-purple);
    font-size:23px;line-height:1.2;text-align:right;margin-bottom:26px}
  .nutrient-list{list-style:none}
  .nutrient-list li{font-size:8.6px;line-height:1.45;color:var(--muted);margin-bottom:9px}
  .nutrient-list b{color:var(--ink);font-weight:600}

  /* inside spread */
  .inside-left{position:absolute;left:0;top:0;width:397px;height:100%}
  .banner{position:relative;height:150px;
    background:linear-gradient(120deg,var(--brand-purple) 0%,var(--purple-mid) 55%,#a58bb8 100%)}
  .banner-text{position:absolute;left:26px;top:38px;color:#fff}
  .banner-brand{font-family:"Josefin Sans",Arial,sans-serif;font-weight:300;font-size:21px;letter-spacing:.5px}
  .banner-title{font-family:"Josefin Sans",Arial,sans-serif;font-weight:700;font-size:40px;line-height:1;margin-top:4px}
  .fold{position:absolute;left:397px;top:0;width:1px;height:100%;background:#e2dce6}
  .inside-right{position:absolute;left:398px;top:0;width:397px;height:100%}
  .curves{position:absolute;left:0;top:0}

  .menu{list-style:none}
  .inside-left .menu{padding:18px 26px 0 26px}
  .inside-right .menu{position:absolute;left:26px;top:150px;width:345px}
  .menu li{margin-bottom:18px}
  .menu h3{font-family:"Montserrat",Arial,sans-serif;font-weight:700;font-size:10px;
    color:var(--brand-purple);text-transform:uppercase;letter-spacing:.4px;margin-bottom:4px;
    display:flex;align-items:center;gap:6px}
  .menu h3 .dot{width:6px;height:6px;background:var(--brand-purple);border-radius:50%;flex:none}
  .menu p{font-size:8.4px;line-height:1.5;color:var(--muted)}
</style>
</head>
<body>

<section class="spread spread--outside">
  <div class="hero-photo" role="img" aria-label="Photo of a relaxed woman seated beside an IV drip bag on a stand"></div>
  <div class="b12-panel">
    <h2 class="b12-title">Dr. Halvorsen's Vitamin<br>B12 Cocktail's<br>Essential Vitamins<br>And Nutrients:</h2>
    <ul class="nutrient-list">
      <li><b>Thiamine</b> – is used by the body to metabolize food for energy and maintain proper heart and nerve function.</li>
      <li><b>Riboflavin</b> – acts as an antioxidant within the body. Riboflavin prevents free radical damage and protects skin and eye health.</li>
      <li><b>Niacinamide</b> – helps maintain a healthy cardiovascular system and metabolism; aids digestion, healthy skin formation, and adds to the prevention of some conditions.</li>
      <li><b>Dexpanthenol</b> – is important for blood development and keeping the nervous and immune systems healthy.</li>
      <li><b>Pyridoxine hydrochloride</b> – helps with DNA synthesis and supports digestion; it also helps the body's use of fats and carbohydrates for energy, and in the making of new proteins.</li>
      <li><b>Methionine</b> – aids in tissue growth and repair, as well as promoting healthy hair, skin, and nails.</li>
      <li><b>Inositol</b> – aids in the metabolic breakdown of fats and helps reduce blood cholesterol.</li>
      <li><b>L-carnitine</b> – helps convert fatty acids into energy.</li>
      <li><b>Chromium</b> – helps move sugars from the blood system, and turn fats, carbs, and proteins into energy.</li>
    </ul>
  </div>
</section>

<section class="spread spread--inside">
  <div class="inside-left">
    <div class="banner" role="img" aria-label="Soft focus photo of an IV drip line in purple tones">
      <div class="banner-text">
        <div class="banner-brand">The Drip Atelier</div>
        <div class="banner-title">IV THERAPY</div>
      </div>
    </div>
    <ul class="menu">
      <li><h3>Immunity Booster $150</h3>
        <p>Have a cold, flu or just need to give your immunity a boost? Let us mix a powerful punch in our booster bag just for you to prevent or relieve aches and pain.</p></li>
      <li><h3>Refresh &amp; Hydrate $100</h3>
        <p>Relieve dehydration from the extremes of lifestyle with our balanced electrolyte cocktail targeting jet lag, fatigue, stress and sports-related activity to leave you feeling more youthful and refreshed.</p></li>
      <li><h3>Migraine Buster $150</h3>
        <p>Eradicate your migraine pain, nausea, vomiting, and light sensitivity with our fast-acting formula.</p></li>
      <li><h3>Wellness Infusion: Wellspring Cocktail $140</h3>
        <p>This infusion of vitamins, minerals and electrolytes results in faster access of these nutrients into your cells, enhancing energy, decreasing stress and anxiety, in addition to improving mood. Other benefits include relief of asthma, depression, allergies and fibromyalgia pain.</p></li>
    </ul>
  </div>
  <div class="fold"></div>
  <div class="inside-right">
    <svg class="curves" width="397" height="140" viewBox="0 0 397 140" aria-hidden="true">
      <path d="M140 0 C 210 60, 300 70, 397 40" fill="none" stroke="var(--purple-soft)" stroke-width="1.2"/>
      <path d="M190 0 C 250 45, 320 55, 397 25" fill="none" stroke="var(--brand-purple)" stroke-width="1"/>
    </svg>
    <ul class="menu">
      <li><h3><span class="dot"></span>Glo $200</h3>
        <p>A beauty infusion of Lumenra. Biotin and our special formula created to strengthen your hair, nails and skin for that special look!</p></li>
      <li><h3><span class="dot"></span>The Ultimate Weight Loss Infusion $200</h3>
        <p>Our unique fat burning formula works best alongside fitness and diet plans to boost metabolism, support energy and help reach goals.</p></li>
      <li><h3><span class="dot"></span>NAD+ IV: The Fountain of Youth $300</h3>
        <p>Anti-aging co-enzyme NAD+ in conjunction with vitamins elevate brain health and beauty, all in one IV treatment!</p></li>
    </ul>
  </div>
</section>

</body>
</html>
```